Lumora business card for a plastic surgeon

we need a business card for plastic surgeons that work on a clinic called LUMORA.
we want a clean design and the following informations: name of the doctor, doctor's registration number (called CRM), telephone, address, facebook, instagram.
Colors: white, blue tones, light brown/ coffee

facebook and instagram: lumoracirurgiaestetica

Industry/Entity Type

Business

Contact Information for Business Card

clean design

Font styles to use
Serif
Sans Serif
Other font styles liked:
• helvetica light

Colors
cee9f5
85cae6
85abd2
3276b5
cfeae6
cedeed
eaf1f7

Requirements
Must have
• doctor's name
• identification number (called CRM)
• contact (phone, facebook, instagram, address)

```html
<!DOCTYPE html>
<html lang="pt">
<head>
<meta charset="utf-8">
<title>Lumora – Cartão de visita</title>
<link rel="stylesheet" href="https://fonts.googleapis.com/css2?family=Cinzel:wght@400&family=Lora:wght@600&family=Roboto:wght@400&display=swap">
<style>
  :root {
    --backdrop: #a9a6a6;
    --card: #f6f7f9;
    --card-front: #eef3fa;
    --aqua: #6bbcd6;
    --navy: #24406b;
    --band-navy: #1f4170;
    --coffee: #ad9482;
    --icon-coffee: #a88a76;
    --divider: #e2e5ea;
  }
  * { box-sizing: border-box; margin: 0; padding: 0; }
  html, body { width: 1200px; height: 1200px; overflow: hidden; }
  body { background: var(--backdrop); position: relative; }

  .card { position: absolute; width: 713px; height: 419px; }
  .card--front { left: 238px; top: 119px; background: var(--card-front); }
  .card--back { left: 230px; top: 644px; height: 418px; background: var(--card); overflow: hidden; }

  .brand { position: absolute; text-align: center; font-family: "Cinzel", serif; font-weight: 400; }
  .brand__name { color: var(--aqua); letter-spacing: 2px; line-height: 1; display: block; }
  .brand__tag { color: var(--navy); letter-spacing: 1px; line-height: 1; display: block; }

  .card--front .brand { left: 0; right: 0; top: 150px; }
  .card--front .brand__name { font-size: 92px; }
  .card--front .brand__tag { font-size: 33px; margin-top: 12px; }

  .card--back .brand { left: 30px; width: 350px; top: 148px; }
  .card--back .brand__name { font-size: 62px; }
  .card--back .brand__tag { font-size: 24px; margin-top: 12px; }

  .divider { position: absolute; left: 349px; top: 60px; width: 1px; height: 272px; background: var(--divider); }

  .contact { position: absolute; left: 384px; top: 86px; color: var(--navy); font-family: "Roboto", sans-serif; }
  .contact__name { font-family: "Lora", serif; font-weight: 600; font-size: 26px; line-height: 1.2; }
  .contact__crm { font-size: 16px; margin-top: 2px; }
  .contact__address { font-size: 18px; line-height: 23px; margin-top: 36px; }
  .contact__list { list-style: none; margin-top: 26px; font-size: 18px; }
  .contact__list li { display: flex; align-items: center; height: 25px; }
  .contact__list svg { width: 18px; height: 14px; margin-left: 0; margin-right: 17px; fill: var(--icon-coffee); }

  .bands { position: absolute; left: 0; bottom: 0; width: 713px; height: 54px; }
  .social { position: absolute; left: 384px; bottom: 16px; display: flex; align-items: center; color: #fff; font-family: "Roboto", sans-serif; font-size: 18px; }
  .social__mark { width: 16px; height: 16px; background: #fff; border-radius: 3px; margin-right: 10px; }
</style>
</head>
<body>

<section class="card card--front">
  <div class="brand">
    <span class="brand__name">LUMORA</span>
    <span class="brand__tag">CIRURGIA PLÁSTICA</span>
  </div>
</section>

<section class="card card--back">
  <div class="brand">
    <span class="brand__name">LUMORA</span>
    <span class="brand__tag">CIRURGIA PLÁSTICA</span>
  </div>

  <div class="divider"></div>

  <div class="contact">
    <p class="contact__name">Dr. Rafael Nunes</p>
    <p class="contact__crm">CRM: 123456789</p>
    <p class="contact__address">Your Long Commercial or<br>business address in 2 line</p>
    <ul class="contact__list">
      <li>
        <svg viewBox="0 0 18 14" aria-hidden="true"><path d="M1 5c0-3 16-3 16 0v1h-4V4H5v2H1z"/><rect x="3" y="7" width="12" height="6" rx="1"/></svg>
        +00 111 222 3333
      </li>
      <li>
        <svg viewBox="0 0 18 14" aria-hidden="true"><circle cx="9" cy="7" r="6" fill="none" stroke="#a88a76" stroke-width="1.4"/><path d="M3 7h12M9 1v12" stroke="#a88a76" stroke-width="1.2"/></svg>
        www.yourwebsite.com
      </li>
      <li>
        <svg viewBox="0 0 18 14" aria-hidden="true"><rect x="1" y="2" width="16" height="10"/><path d="M1 2l8 6 8-6" fill="none" stroke="#f6f7f9" stroke-width="1.4"/></svg>
        yourname@yourwebsite.com
      </li>
    </ul>
  </div>

  <svg class="bands" viewBox="0 0 713 54" aria-hidden="true">
    <rect x="0" y="26" width="330" height="28" fill="var(--coffee)"/>
    <polygon points="330,0 713,0 713,54 305,54" fill="var(--band-navy)"/>
  </svg>
  <div class="social">
    <span class="social__mark"></span>
    lumoracirurgiaestetica
  </div>
</section>

</body>
</html>
```